Business cards, stationary, envelopes and fax cover sheet
for Tessaline Goods
Simple
Corin Maddox
Founder, VP Operations and Marketing
P.O. Box 4682
Wildomar, CA 92871
corin@tessalinegoods.example
www.tessalinegoods.example
the logo on the backside
Business Logo
Business Symbol
Company name alone
logo in ai format
symbol in ai format
company name alone in ai format

```html
<!DOCTYPE html>
<html lang="en">
<head>
<meta charset="utf-8">
<title>Tessaline Goods Stationery</title>
<link href="https://fonts.googleapis.com/css2?family=Open+Sans:wght@400;600;700&display=swap" rel="stylesheet">
<style>
:root{
  --bg:#e6e3de;
  --paper:#ffffff;
  --green-light:#8cc63f;
  --blue:#1d5fa8;
  --ink:#333333;
  --muted:#777777;
  --rule:#bbbbbb;
  --label:#4a4a4a;
}
*{box-sizing:border-box;margin:0;padding:0}
html,body{width:1200px;height:559px;overflow:hidden}
body{background:var(--bg);font-family:"Open Sans",Arial,sans-serif;color:var(--ink);position:relative}
.sheet-label{position:absolute;font-size:7px;color:var(--label);text-align:center}
.paper{position:absolute;background:var(--paper);box-shadow:0 1px 4px rgba(0,0,0,.25);overflow:hidden}
.brand{display:flex;align-items:center;justify-content:center;color:var(--ink);font-weight:600;letter-spacing:.5px}
.wave{position:absolute;left:0;bottom:0;width:100%}
.body-text{font-size:5.2px;line-height:1.55;color:var(--ink)}
.body-text p{margin-bottom:5px}
.footer-line{position:absolute;bottom:6px;left:0;width:100%;text-align:center;font-size:4.6px;color:#fff}
.signature{width:48px;height:12px;background:linear-gradient(90deg,#9aa3b5,#cfd5e0);border-radius:6px;margin:4px 0 2px}

/* fax */
.fax{left:24px;top:19px;width:288px;height:533px}
.fax .brand{position:absolute;top:24px;left:0;width:100%;font-size:14px}
.fax-title{position:absolute;top:62px;right:22px;font-size:9px;font-weight:700;color:var(--ink)}
.fax-table{position:absolute;top:76px;left:22px;width:244px;border-collapse:collapse;font-size:5px}
.fax-table td{border:0.6px solid var(--rule);height:11px;padding:0 3px;width:25%}
.fax-checks{position:absolute;top:128px;left:22px;width:244px;display:flex;justify-content:space-between;font-size:5px}
.fax-checks span::before{content:"";display:inline-block;width:5px;height:5px;border:0.6px solid var(--ink);margin-right:2px;vertical-align:-1px}
.fax .body-text{position:absolute;top:148px;left:22px;width:244px}

/* letterhead */
.letter{left:348px;top:19px;width:276px;height:533px}
.letter .brand{position:absolute;top:24px;left:0;width:100%;font-size:14px}
.letter .body-text{position:absolute;top:68px;left:24px;width:228px}

/* cards */
.card{width:150px;height:82px;top:36px}
.card-front{left:826px}
.card-front .brand{height:100%;font-size:13px}
.card-back{left:1000px}
.card-back .brand{position:absolute;top:9px;left:10px;justify-content:flex-start;font-size:8px}
.card-info{position:absolute;top:22px;left:10px;font-size:4.4px;line-height:1.45}
.card-info .name{font-size:6px;font-weight:700;color:var(--blue)}
.card-info .title{color:var(--muted);margin-bottom:2px}

/* envelope */
.envelope{left:826px;top:252px;width:326px;height:134px}
.envelope .brand{position:absolute;top:12px;left:14px;justify-content:flex-start;font-size:10px}
.return-address{position:absolute;top:28px;left:14px;font-size:4.8px;line-height:1.5}
</style>
</head>
<body>

<div class="sheet-label" style="left:24px;top:6px;width:288px">Fax Cover</div>
<div class="sheet-label" style="left:348px;top:6px;width:276px">Letterhead</div>
<div class="sheet-label" style="left:826px;top:25px;width:150px">Business Card (Front)</div>
<div class="sheet-label" style="left:1000px;top:25px;width:150px">Business Card (Back)</div>
<div class="sheet-label" style="left:826px;top:240px;width:326px">Envelope</div>

<section class="paper fax">
  <div class="brand">Tessaline</div>
  <div class="fax-title">FAX</div>
  <table class="fax-table">
    <tr><td>To:</td><td></td><td>From:</td><td></td></tr>
    <tr><td>Fax:</td><td></td><td>Pages:</td><td></td></tr>
    <tr><td>Phone:</td><td></td><td>Date:</td><td></td></tr>
    <tr><td>Re:</td><td></td><td>CC:</td><td></td></tr>
  </table>
  <div class="fax-checks">
    <span>Urgent</span><span>For Review</span><span>Please Comment</span><span>Please Reply</span><span>Please Recycle</span>
  </div>
  <div class="body-text">
    <p>Thank you for your recent order. We have reviewed the details and prepared a summary of items, quantities and delivery dates for your approval. Please check each line carefully and let us know of any changes before the end of the week so we can schedule production on time.</p>
    <p>Our team remains available to answer questions about materials, sizing and installation. We appreciate your business and look forward to working with you again.</p>
    <p>Sincerely,</p>
    <div class="signature" role="img" aria-label="Handwritten signature"></div>
    <p><strong>Corin Maddox</strong></p>
  </div>
  <svg class="wave" viewBox="0 0 288 44" height="44" preserveAspectRatio="none">
    <path d="M0 14 C80 0 180 30 288 8 V44 H0Z" fill="var(--green-light)"/>
    <path d="M0 22 C90 8 190 36 288 16 V44 H0Z" fill="var(--blue)"/>
  </svg>
  <div class="footer-line">P.O. Box 4682 · Wildomar, CA 92871 · www.tessalinegoods.example</div>
</section>

<section class="paper letter">
  <div class="brand">Tessaline</div>
  <div class="body-text">
    <p>Month Day, Year</p>
    <p>Customer Name<br>Company Name<br>123 Main Street<br>City, State Zip</p>
    <p>Dear Customer Name,</p>
    <p>Thank you for your recent order. We have reviewed the details and prepared a summary of items, quantities and delivery dates for your approval. Please check each line carefully and let us know of any changes before the end of the week so we can schedule production on time.</p>
    <p>Our team remains available to answer questions about materials, sizing and installation. We appreciate your business and look forward to working with you again.</p>
    <p>Please keep this letter for your records and contact us with any further needs.</p>
    <p>Sincerely,</p>
    <div class="signature" role="img" aria-label="Handwritten signature"></div>
    <p><strong>Corin Maddox</strong></p>
  </div>
  <svg class="wave" viewBox="0 0 276 44" height="44" preserveAspectRatio="none">
    <path d="M0 14 C80 0 170 30 276 8 V44 H0Z" fill="var(--green-light)"/>
    <path d="M0 22 C90 8 180 36 276 16 V44 H0Z" fill="var(--blue)"/>
  </svg>
  <div class="footer-line">P.O. Box 4682 · Wildomar, CA 92871 · www.tessalinegoods.example</div>
</section>

<section class="paper card card-front">
  <div class="brand">Tessaline</div>
</section>

<section class="paper card card-back">
  <div class="brand">Tessaline</div>
  <div class="card-info">
    <div class="name">Corin Maddox</div>
    <div class="title">Founder, VP Operations and Marketing</div>
    <div>P.O. Box 4682, Wildomar, CA 92871</div>
    <div>corin@tessalinegoods.example</div>
    <div>www.tessalinegoods.example</div>
  </div>
  <svg class="wave" viewBox="0 0 150 16" height="16" preserveAspectRatio="none">
    <path d="M0 6 C45 0 95 14 150 3 V16 H0Z" fill="var(--green-light)"/>
    <path d="M0 10 C50 3 100 17 150 7 V16 H0Z" fill="var(--blue)"/>
  </svg>
</section>

<section class="paper envelope">
  <div class="brand">Tessaline</div>
  <div class="return-address">
    <div>P.O. Box 4682</div>
    <div>Wildomar, CA 92871</div>
    <div>www.tessalinegoods.example</div>
  </div>
  <svg class="wave" viewBox="0 0 326 26" height="26" preserveAspectRatio="none">
    <path d="M0 9 C100 0 210 21 326 5 V26 H0Z" fill="var(--green-light)"/>
    <path d="M0 14 C110 5 220 26 326 10 V26 H0Z" fill="var(--blue)"/>
  </svg>
</section>

</body>
</html>
```